Business card for a plastic surgeon

i need a business card for a plastic surgeon. I have two adresses. The card should communicate safety, simmetry, beauty and with soft colors.
What i want in the card:
- my logo: Letters "R"and "B" (picture uploaded)
- my name: Renato Bastiani
- my registration: CRM 507 219
- my adresses and phone numbers (2):
- Av Dr Teixeira Lopes, 2710, sala 305 - Vila Olímpia | São Paulo/ SP - Phone: 11 4172-5036
- Al. Itapeva, 47, 3 andar - Alphaville | Barueri/ SP - Phone: 11 6350-2481

- my social network: site, facebook and instagram

Target Market(s)

people (95% girls and women) that want cosmetic procedures and plastic surgery

Industry/Entity Type

Business

Contact Information for Business Card

The card should communicate safety, simmetry, beauty and with soft colors.
Beige, brown, gray, rosy are some options. Color is free

Font styles to use
Serif

Requirements
Must have
• - my logo: Letters "R"and "B" (picture uploaded)
• - my name: Renato Bastiani
• - my registration: CRM 507 219
• - my adresses and phone numbers (2):
• - Av Dr Teixeira Lopes, 2710, sala 305 - Vila Olímpia | São Paulo/ SP - Phone: 11 4172-5036
• - Al. Itapeva, 47, 3 andar - Alphaville | Barueri/ SP - Phone: 11 6350-2481
• - my social network: site, facebook and instagram
Should not have
• other images (only my logo)

```html
<!DOCTYPE html>
<html lang="pt">
<head>
<meta charset="utf-8">
<title>Renato Bastiani – Cartão de Visita</title>
<link rel="stylesheet" href="https://fonts.googleapis.com/css2?family=Cinzel:wght@400;700&family=Tinos:wght@400;700&display=swap">
<style>
  :root {
    --stage: #3b3b3d;
    --brown: #82553b;
    --paper: #ffffff;
    --mist: #d9d9d9;
    --ink: #4a4a4a;
    --ink-soft: #5a5a5a;
    --white: #ffffff;
  }
  * { box-sizing: border-box; margin: 0; padding: 0; }
  html, body {
    width: 1200px; height: 900px; overflow: hidden;
    background: var(--stage);
  }
  .stage { position: relative; width: 1200px; height: 900px; }

  .card {
    position: absolute;
    width: 620px; height: 354px;
    box-shadow: 0 10px 28px rgba(0,0,0,.45);
    overflow: hidden;
  }

  /* back side */
  .card--back {
    left: 470px; top: 80px;
    background: var(--brown);
    display: flex; align-items: center; justify-content: center;
  }
  .monogram-name {
    font-family: "Cinzel", serif;
    font-weight: 400;
    font-size: 26px;
    letter-spacing: 3px;
    color: var(--white);
  }

  /* front side */
  .card--front {
    left: 110px; top: 440px;
    background: var(--paper);
  }
  .card__field { position: absolute; inset: 0; }

  .headline { position: absolute; left: 34px; top: 30px; }
  .headline__name {
    font-family: "Cinzel", serif;
    font-weight: 400;
    font-size: 25px;
    letter-spacing: 1px;
    color: var(--ink-soft);
  }
  .headline__role {
    font-family: "Cinzel", serif;
    font-size: 13px;
    letter-spacing: 6.5px;
    color: var(--ink-soft);
    margin-top: 2px;
    padding-left: 60px;
  }

  .details {
    position: absolute; left: 34px; top: 112px;
    font-family: "Tinos", serif;
    color: var(--ink);
    font-size: 13px;
    line-height: 16px;
  }
  .details__name {
    font-family: "Cinzel", serif;
    font-weight: 700;
    font-size: 16px;
    letter-spacing: .5px;
  }
  .details__reg {
    font-family: "Cinzel", serif;
    font-size: 11.5px;
    letter-spacing: .8px;
    margin-bottom: 4px;
  }
  .details__office + .details__office { margin-top: 4px; }

  .card__mark {
    position: absolute; left: 390px; top: 200px;
    font-family: "Cinzel", serif;
    font-size: 22px;
    letter-spacing: 2px;
    color: var(--ink);
  }

  .social {
    position: absolute; right: 26px; bottom: 20px;
    display: flex; align-items: center; gap: 6px;
    font-family: "Tinos", serif;
    font-size: 13px;
    color: var(--ink);
  }
  .social__dot {
    width: 8px; height: 8px; border-radius: 50%;
    background: var(--ink);
  }
</style>
</head>
<body>
<main class="stage">

  <section class="card card--back" aria-label="Verso do cartão">
    <span class="monogram-name">Renato Bastiani</span>
  </section>

  <section class="card card--front" aria-label="Frente do cartão">
    <svg class="card__field" width="620" height="354" viewBox="0 0 620 354" aria-hidden="true">
      <path d="M620 128 C 470 128, 410 200, 372 262 C 335 322, 265 354, 200 354 L 620 354 Z" fill="var(--mist)"/>
    </svg>

    <header class="headline">
      <h1 class="headline__name">DR. RENATO BASTIANI</h1>
      <p class="headline__role">CIRURGIÃO PLÁSTICO</p>
    </header>

    <div class="details">
      <p class="details__name">RENATO BASTIANI</p>
      <p class="details__reg">Registration N: CRM 507 219</p>
      <p class="details__office">Av Dr Teixeira Lopes, 2710, sala 305<br>Vila Olímpia | São Paulo/ SP<br>P: 11 4172-5036</p>
      <p class="details__office">Al. Itapeva, 47, 3 andar - Alphaville | Barueri/ SP<br>P: 11 6350-2481</p>
    </div>

    <span class="card__mark">Renato Bastiani</span>

    <div class="social">
      <span class="social__dot"></span>
      <span>@drbastiani</span>
    </div>
  </section>

</main>
</body>
</html>
```